Business card design for strategy and management consulting company. Would like to have a clean and professional business card, based on the attached logo. The company is a strategy and management consulting company focusing on sustainable business modlels based on economic, social and environmental market opportunities. Preferably the logo should be included on both sides of the design.

Industry/Entity Type

Business

Contact Information for Business Card

Håvard Lilleby, CEO/Management consultant
havard.lilleby@quarvenpartners.example
Mob: +47 948 26 317
Office: Vikfjell gate 14, pb 312 sentrum, N-0172 Oslo Norway

Requirements
Must have
• Include attached logo
Nice to have
• Would like to have the logo on both sides
Should not have
• Many colours.

```html
<!DOCTYPE html>
<html lang="en">
<head>
<meta charset="utf-8">
<title>Quarven – Business Card</title>
<link rel="stylesheet" href="https://fonts.googleapis.com/css2?family=Source+Sans+3:wght@400;600;700&display=swap">
<style>
  :root {
    --backdrop: #3b3431;
    --card: #0e0e0e;
    --ink: #ffffff;
    --accent: #f2d21b;
    --rule: #7a7a7a;
  }
  * { margin: 0; padding: 0; box-sizing: border-box; }
  html, body {
    width: 1200px;
    height: 844px;
    overflow: hidden;
    background: var(--backdrop);
    font-family: "Source Sans 3", Arial, sans-serif;
  }
  .stage {
    width: 1200px;
    height: 844px;
    display: flex;
    align-items: center;
    justify-content: center;
    gap: 40px;
  }
  .card {
    position: relative;
    width: 540px;
    height: 310px;
    background: var(--card);
    color: var(--ink);
    border-radius: 3px;
    box-shadow: 0 10px 30px rgba(0,0,0,0.45);
  }
  .brand {
    position: absolute;
    left: 0;
    right: 0;
    text-align: center;
    font-weight: 600;
    font-size: 78px;
    line-height: 1;
    color: var(--ink);
  }
  .card--front .brand { top: 72px; }
  .card--back .brand { top: 88px; }
  .contact-row {
    position: absolute;
    top: 205px;
    left: 0;
    right: 0;
    display: flex;
    align-items: stretch;
  }
  .person {
    width: 248px;
    text-align: right;
    padding-right: 14px;
  }
  .person__name {
    color: var(--accent);
    font-weight: 700;
    font-size: 17px;
    line-height: 1.25;
  }
  .person__role {
    font-size: 15px;
    line-height: 1.3;
  }
  .divider {
    width: 1px;
    background: var(--rule);
  }
  .channels {
    list-style: none;
    padding-left: 12px;
    font-size: 13px;
    line-height: 1.6;
  }
  .channels li {
    display: flex;
    align-items: center;
    gap: 8px;
  }
  .channels svg { flex: none; }
  .address {
    position: absolute;
    right: 100px;
    top: 196px;
    text-align: right;
    font-size: 14px;
    line-height: 1.35;
    font-style: normal;
  }
</style>
</head>
<body>
<main class="stage">
  <section class="card card--front">
    <p class="brand">Quarven</p>
    <div class="contact-row">
      <div class="person">
        <p class="person__name">Håvard Lilleby</p>
        <p class="person__role">CEO/Management consultant</p>
      </div>
      <span class="divider"></span>
      <ul class="channels">
        <li>
          <svg width="9" height="14" viewBox="0 0 9 14" aria-hidden="true">
            <rect x="0.75" y="0.75" width="7.5" height="12.5" rx="1.5" fill="none" stroke="var(--accent)" stroke-width="1.5"/>
            <circle cx="4.5" cy="11" r="0.9" fill="var(--accent)"/>
          </svg>
          <span>+47 948 26 317</span>
        </li>
        <li>
          <svg width="13" height="10" viewBox="0 0 13 10" aria-hidden="true">
            <rect x="0" y="0" width="13" height="10" rx="1" fill="var(--accent)"/>
            <path d="M1 1 L6.5 5.5 L12 1" fill="none" stroke="var(--card)" stroke-width="1.2"/>
          </svg>
          <span>havard.lilleby@quarvenpartners.example</span>
        </li>
      </ul>
    </div>
  </section>

  <section class="card card--back">
    <p class="brand">Quarven</p>
    <address class="address">
      Vikfjell gate 14,<br>
      pb 312 sentrum, N-0172 Oslo Norway
    </address>
  </section>
</main>
</body>
</html>
```